Web site for fans of TV series "The Drover's Son"

1. Description: This is a new web site for the fans of a Western TV series called "The Drover's Son". It ran for nine seasons from 1962 to 1971.

It is going to be a fan-generated content. The site will use a proprietary social-sharing software in the back-end. The software could be looked as your personal Pagebook service running on your own domain. In fact, anyone can use this software for any social-sharing need.

A sample of the software running a social-sharing site:
http://www.velmasite.example

The public-facing software has ten sections or modules as follows:

1. Survey
2. Blog
3. Links
4. Video
5. Music
6. Photo
7. Cartoon
8. Photo Album
9. Quotes
10. Follow/Followers (like chirpr)

2. Delivery. Three designs for three pages. I need delivery in PSD, JPG and AI formats..

3. Pages

3.1. Homepage
Example: http://www.velmasite.example

IMPORTANT REQUIREMENT. The Homepage should be designed such that I or the site Admin with basic knowledge of HTML and CSS can move around different sections or modules without a need to rewrite the CSS or HTML code.

3.2. Point of Entry or Summary page.
Example: http://velmasite.example/qwpd/blog/latest/

3.3. Detail page
Example: http://velmasite.example/qwpd/blog/2929/
Updates

Project Deadline Extended
Reason: I received acceptable designs late. I would like to give this contest 7 more days. This gives me time to work with current designs and just in case I receive new designs.

Target Market(s)

Age: Above 40, average age is 50-55

Gender: Primarily female

Location: Primarily United States, but we have a visible following in Europe and South America.

Industry/Entity Type

Tv

Requirements
Must have
• 1. The image/icon of The Drover's Son. You can capture it via ClipTube clips at the opening of the show.

2. Red color (burgundy. See shirt of the main character called Drover played by actor Harold Penwick.

3. The American West spirit (yes, you may call it the cowboy spirit)

4. The Homepage should be designed such that a person with basic knowledge of CSS and HTML coding can move around different sections or modules.
Should not have
• No cartoonish icons.

```html
<!DOCTYPE html>
<html lang="en">
<head>
<meta charset="utf-8">
<title>The Drover's Son Wiki</title>
<link rel="stylesheet" href="https://fonts.googleapis.com/css2?family=Oswald:wght@500;700&family=Kaushan+Script&family=Montserrat:wght@600;700&family=Arimo:wght@400;700&display=swap">
<style>
:root{
  --burgundy:#9c2a22;
  --burgundy-dark:#7a1c17;
  --parchment:#f1cf8e;
  --parchment-deep:#e2b062;
  --charcoal:#4a4440;
  --ink:#3b2e25;
  --muted:#7a6a58;
  --rule:#c9a066;
  --olive:#a99a6a;
  --white:#fff;
}
*{box-sizing:border-box;margin:0;padding:0}
html,body{width:730px;height:1200px;overflow:hidden}
body{
  position:relative;font-family:"Arimo",Arial,sans-serif;color:var(--ink);
  background:
    radial-gradient(ellipse 60% 40% at 8% 18%,rgba(150,110,60,.35),transparent 70%),
    radial-gradient(ellipse 50% 30% at 95% 10%,rgba(150,110,60,.4),transparent 70%),
    radial-gradient(ellipse 70% 50% at 50% 55%,#f6d99c,transparent 80%),
    linear-gradient(180deg,#e9c384 0%,var(--parchment) 30%,var(--parchment) 85%,var(--parchment-deep) 100%);
}
.abs{position:absolute}
/* header */
.brand{left:162px;top:16px;display:flex;align-items:center;gap:5px;font:700 11px "Arimo",sans-serif;color:var(--burgundy-dark);white-space:nowrap}
.brand-mark{width:9px;height:9px;background:var(--burgundy-dark)}
.account{top:8px;right:175px;display:flex;gap:3px}
.account a{font:600 6.5px "Montserrat",sans-serif;color:var(--white);text-decoration:none;padding:3px 6px;text-transform:uppercase;background:var(--olive)}
.account a.manage{background:var(--burgundy)}
.main-nav{left:270px;top:33px;width:288px;height:15px;background:var(--burgundy);display:flex;justify-content:space-around;align-items:center;
  clip-path:polygon(0 10%,3% 0,50% 8%,97% 0,100% 15%,99% 90%,60% 100%,2% 92%)}
.main-nav a{font:600 5.5px "Montserrat",sans-serif;color:var(--white);text-decoration:none}
/* hero */
.hero{left:158px;top:64px;width:387px;height:250px;
  background:linear-gradient(180deg,#5a8fc7 0%,#a9c6df 35%,#b0764a 60%,#7a8a3e 85%,#c9a064 100%);
  clip-path:polygon(1% 2%,50% 0,99% 3%,100% 60%,97% 96%,50% 100%,3% 97%,0 50%)}
.hero-title{left:198px;top:146px;font:500 22px "Oswald",sans-serif;color:var(--white)}
.hero-arrow{width:14px;height:14px;border-radius:50%;background:var(--burgundy);top:177px}
.dots{left:353px;top:313px;display:flex;gap:2px}
.dots span{width:5px;height:5px;border-radius:50%;background:#9a8e80}
.divider{height:2px;background:var(--burgundy-dark);opacity:.6}
/* section banners */
.banner{height:24px;display:flex;align-items:center;padding-left:9px;font:13px "Kaushan Script",cursive;color:var(--white);
  clip-path:polygon(0 12%,4% 0,40% 8%,70% 2%,100% 10%,98% 50%,100% 92%,60% 100%,25% 92%,2% 100%,1% 55%)}
.banner.red{background:var(--burgundy)}
.banner.grey{background:var(--charcoal)}
.banner.sm{height:20px;font-size:11px}
/* survey */
.avatar{background:linear-gradient(160deg,#b89a82,#6e5547);border:1px solid #fff}
.question{left:185px;top:386px;font:400 7px "Arimo",sans-serif}
.question b{font-size:11px}
.option{font-size:6px;color:var(--muted);display:flex;gap:6px;align-items:center}
.option i{width:6px;height:6px;border-radius:50%;background:#b9ad9c;display:inline-block}
.option i.on{background:#555}
.btn-submit{left:162px;top:435px;background:var(--olive);color:#fff;font:700 6.5px "Arimo",sans-serif;padding:4px 8px;text-transform:uppercase}
.view-all{left:310px;top:466px;font:9px "Kaushan Script",cursive;color:var(--burgundy)}
.dotted{border-top:1px dotted var(--rule)}
/* blog */
.blog{left:162px;width:218px;height:44px;display:flex;gap:6px}
.blog .avatar{width:28px;height:28px;flex:none}
.blog h3{font:700 6.5px "Arimo",sans-serif;color:var(--burgundy)}
.blog p{font-size:4.6px;color:var(--muted);line-height:1.3;margin:1px 0 3px}
.blog .foot{display:flex;justify-content:space-between;font-size:4.5px}
.blog .foot b{color:var(--ink)}
.blog .foot span{color:var(--burgundy)}
.pager{display:flex;gap:4px}
.pager span{width:10px;height:8px;background:#f5e3bd;border:1px solid #d6bd90;font-size:4.5px;display:flex;align-items:center;justify-content:center;color:var(--muted)}
.pager span.wide{width:14px}
.pager span.on{background:#7a7066;color:#fff}
.thumb{border:2px solid #eee;background:linear-gradient(160deg,#b4aaa0,#5e554d)}
.thumb.warm{background:linear-gradient(160deg,#c7a3a0,#7c4a45)}
/* right column media */
.video{left:421px;width:135px;height:80px;background:linear-gradient(160deg,#6a5240,#2e231b)}
.play{position:absolute;left:52px;top:24px;width:26px;height:26px;border-radius:50%;background:rgba(120,120,120,.7)}
.play::after{content:"";position:absolute;left:10px;top:7px;border-left:9px solid #eee;border-top:6px solid transparent;border-bottom:6px solid transparent}
.controls{position:absolute;bottom:0;left:0;right:0;height:8px;background:#111}
.controls::before{content:"";position:absolute;left:6px;top:3px;width:75px;height:2px;background:#b32020}
.meta{left:421px;display:flex;gap:4px;font-size:4.2px;color:var(--muted);align-items:center}
.meta .avatar{width:12px;height:12px}
.music{left:421px;top:645px;width:135px;height:60px;background:#fbf7ef}
.cartoon{left:421px;top:760px;width:130px;height:70px;background:linear-gradient(160deg,#f6ef9a,#d7c35c)}
/* album */
.album-arrow{width:14px;height:14px;background:var(--burgundy);top:950px}
/* quotes */
.quotes-title{left:0;width:730px;top:1008px;text-align:center;font:14px "Kaushan Script",cursive;color:var(--burgundy)}
.quote{top:1032px;width:168px;display:flex;gap:6px}
.quote .avatar{width:32px;height:32px;flex:none}
.quote p{font-size:5.5px;line-height:1.25}
.quote b{display:block;color:var(--burgundy);font:italic 700 5.5px "Arimo",sans-serif;margin-top:2px}
/* footer */
.footer{left:0;top:1095px;width:730px;height:105px;background:var(--burgundy);
  clip-path:polygon(0 4%,5% 0,15% 3%,30% 0,45% 4%,60% 1%,75% 4%,90% 0,100% 3%,100% 100%,0 100%)}
.fcol{top:1112px;color:#f3d7c6}
.fcol h4{font:700 6.5px "Arimo",sans-serif;color:#fff;margin-bottom:5px}
.fcol li{list-style:none;font-size:5px;line-height:9px}
.social{display:flex;gap:3px;align-items:center;margin-bottom:4px;font-size:4.5px}
.social i{width:20px;height:7px;background:#e9e4ee;display:inline-block}
.social u{text-decoration:none;background:#fff;color:#555;padding:0 2px}
.fbrand{left:474px;top:1134px;display:flex;align-items:center;gap:4px;font:700 8px "Arimo",sans-serif;color:#5e1511;white-space:nowrap}
.fbrand .brand-mark{width:7px;height:7px;background:#5e1511}
.legal{top:1188px;font-size:4.8px;color:#f3d7c6}
</style>
</head>
<body>

<!-- header -->
<div class="abs brand"><span class="brand-mark"></span>The Drover's Son</div>
<nav class="abs account"><a class="manage" href="#">Manage Content</a><a href="#">Login</a><a href="#">Register</a></nav>
<nav class="abs main-nav"><a href="#">SURVEY</a><a href="#">BLOG</a><a href="#">LINKS</a><a href="#">VIDEO</a><a href="#">MUSIC</a><a href="#">PHOTO</a><a href="#">CARTOON</a><a href="#">PHOTO ALBUM</a><a href="#">QUOTES</a></nav>

<!-- hero -->
<div class="abs hero" role="img" aria-label="Three cowboys in hats posed before a desert mountain landscape under a blue sky"></div>
<div class="abs hero-title">THE DROVER'S SON</div>
<svg class="abs hero-arrow" style="left:173px" viewBox="0 0 14 14"><path d="M8 4 5 7l3 3" stroke="#fff" stroke-width="1.5" fill="none"/></svg>
<svg class="abs hero-arrow" style="left:520px" viewBox="0 0 14 14"><path d="M6 4l3 3-3 3" stroke="#fff" stroke-width="1.5" fill="none"/></svg>
<div class="abs dots"><span></span><span></span><span></span><span></span></div>
<div class="abs divider" style="left:326px;top:324px;width:78px"></div>

<!-- featured survey -->
<div class="abs banner red" style="left:160px;top:347px;width:218px">Featured Survey</div>
<div class="abs avatar" style="left:162px;top:381px;width:18px;height:18px" role="img" aria-label="Member portrait"></div>
<div class="abs question"><b>Q:</b> Which of the following Cowboy rides more Bulls?</div>
<div class="abs option" style="left:162px;top:405px"><i></i>Walt Hedley</div>
<div class="abs option" style="left:162px;top:418px"><i class="on"></i>Cora Pell</div>
<div class="abs option" style="left:270px;top:405px"><i></i>Amos Rusk</div>
<div class="abs option" style="left:270px;top:418px"><i></i>Jed Farlow</div>
<div class="abs" style="left:243px;top:404px;height:22px;border-left:1px dotted var(--rule)"></div>
<div class="abs btn-submit">Sumit your answer!</div>
<div class="abs dotted" style="left:162px;top:457px;width:218px"></div>
<div class="abs view-all">View all surveys</div>
<div class="abs dotted" style="left:162px;top:483px;width:218px"></div>

<!-- blogs -->
<div class="abs banner grey" style="left:162px;top:498px;width:215px;padding-left:12px">Blogs</div>
<article class="abs blog" style="top:540px"><div class="avatar" role="img" aria-label="Blogger portrait"></div><div><h3>Lorem Ipsum is simply dummy text of the printing industry.</h3><p>Lorem Ipsum is simply dummy text of the printing and typesetting industry. Lorem Ipsum has been the industry's standard dummy text ever since the 1500s.</p><div class="foot"><b>Read Full Blog</b><span>6 Hour Ago | Like | Share | Comment</span></div></div></article>
<article class="abs blog" style="top:589px"><div class="avatar" role="img" aria-label="Blogger portrait"></div><div><h3>Lorem Ipsum is simply dummy text of the printing industry.</h3><p>Lorem Ipsum is simply dummy text of the printing and typesetting industry. Lorem Ipsum has been the industry's standard dummy text ever since the 1500s.</p><div class="foot"><b>Read Full Blog</b><span>6 Hour Ago | Like | Share | Comment</span></div></div></article>
<article class="abs blog" style="top:639px"><div class="avatar" role="img" aria-label="Blogger portrait"></div><div><h3>Lorem Ipsum is simply dummy text of the printing industry.</h3><p>Lorem Ipsum is simply dummy text of the printing and typesetting industry. Lorem Ipsum has been the industry's standard dummy text ever since the 1500s.</p><div class="foot"><b>Read Full Blog</b><span>6 Hour Ago | Like | Share | Comment</span></div></div></article>
<article class="abs blog" style="top:689px"><div class="avatar" role="img" aria-label="Blogger portrait"></div><div><h3>Lorem Ipsum is simply dummy text of the printing industry.</h3><p>Lorem Ipsum is simply dummy text of the printing and typesetting industry. Lorem Ipsum has been the industry's standard dummy text ever since the 1500s.</p><div class="foot"><b>Read Full Blog</b><span>6 Hour Ago | Like | Share | Comment</span></div></div></article>
<div class="abs dotted" style="left:162px;top:730px;width:218px"></div>
<div class="abs pager" style="left:206px;top:738px"><span class="wide">«</span><span>1</span><span>2</span><span class="on">3</span><span>4</span><span>7</span><span>8</span><span>9</span><span class="wide">»</span></div>

<!-- photo section -->
<div class="abs banner grey" style="left:160px;top:773px;width:223px">Photo Section</div>
<div class="abs thumb" style="left:162px;top:802px;width:51px;height:49px" role="img" aria-label="Black and white photo of a rider on horseback"></div>
<div class="abs thumb warm" style="left:220px;top:802px;width:51px;height:49px" role="img" aria-label="Sepia group photo of cowboys"></div>
<div class="abs thumb" style="left:277px;top:802px;width:51px;height:49px" role="img" aria-label="Cowboy seen from behind under a cloudy sky"></div>
<div class="abs thumb" style="left:334px;top:802px;width:51px;height:49px" role="img" aria-label="Close-up of a revolver"></div>
<div class="abs" style="left:401px;top:350px;height:510px;border-left:1px dotted var(--rule)"></div>

<!-- right column -->
<div class="abs banner grey sm" style="left:418px;top:349px;width:136px">Videos</div>
<div class="abs video" style="top:377px" role="img" aria-label="Video still of riders on horseback"><span class="play"></span><span class="controls"></span></div>
<div class="abs meta" style="top:462px"><span class="avatar" role="img" aria-label="Member portrait"></span><span>Sam Tolliver<br>6 Hour Ago | Like | Share | Comment</span></div>
<div class="abs dotted" style="left:421px;top:480px;width:135px"></div>
<div class="abs video" style="top:490px" role="img" aria-label="Video still of riders on horseback"><span class="play"></span><span class="controls"></span></div>
<div class="abs meta" style="top:574px"><span class="avatar" role="img" aria-label="Member portrait"></span><span>Sam Tolliver<br>6 Hour Ago | Like | Share | Comment</span></div>
<div class="abs pager" style="left:425px;top:598px"><span class="wide">«</span><span>1</span><span>2</span><span class="on">3</span><span>4</span><span>7</span><span>8</span><span>9</span><span class="wide">»</span></div>

<div class="abs banner grey sm" style="left:418px;top:626px;width:136px">Drover Music</div>
<div class="abs music">
  <svg width="135" height="60" viewBox="0 0 135 60"><rect x="6" y="14" width="123" height="2" fill="#bbb"/><rect x="6" y="14" width="45" height="2" fill="#666"/><circle cx="46" cy="15" r="3" fill="#eee" stroke="#888"/><circle cx="50" cy="33" r="6" fill="#555"/><path d="M52 30l-4 3 4 3z" fill="#fff"/><circle cx="85" cy="33" r="6" fill="#555"/><path d="M83 30l4 3-4 3z" fill="#fff"/><circle cx="67" cy="33" r="10" fill="#9c2a22"/><path d="M64 27l9 6-9 6z" fill="#fff"/></svg>
</div>
<div class="abs meta" style="top:711px"><span class="avatar" role="img" aria-label="Member portrait"></span><span>Sam Tolliver<br>6 Hour Ago | Like | Share | Comment</span></div>

<div class="abs banner red sm" style="left:418px;top:742px;width:136px">Drover Cartoons</div>
<div class="abs cartoon" role="img" aria-label="Comic illustration of two cowboys facing off"><span class="play" style="left:53px;top:22px;width:16px;height:16px;background:var(--burgundy)"></span></div>
<div class="abs meta" style="top:838px"><span class="avatar" role="img" aria-label="Member portrait"></span><span>Sam Tolliver<br>6 Hour Ago | Like | Share | Comment</span></div>

<div class="abs divider" style="left:321px;top:867px;width:78px"></div>

<!-- photo album -->
<div class="abs banner red" style="left:160px;top:892px;width:395px">Photo Album</div>
<svg class="abs album-arrow" style="left:162px" viewBox="0 0 14 14"><path d="M8 4 5 7l3 3z" fill="#fff"/></svg>
<svg class="abs album-arrow" style="left:541px" viewBox="0 0 14 14"><path d="M6 4l3 3-3 3z" fill="#fff"/></svg>
<div class="abs thumb" style="left:203px;top:934px;width:48px;height:46px" role="img" aria-label="Rider on horseback"></div>
<div class="abs thumb warm" style="left:255px;top:934px;width:48px;height:46px" role="img" aria-label="Sepia group photo"></div>
<div class="abs thumb" style="left:307px;top:934px;width:48px;height:46px" role="img" aria-label="Cowboy under cloudy sky"></div>
<div class="abs thumb" style="left:359px;top:934px;width:48px;height:46px" role="img" aria-label="Revolver close-up"></div>
<div class="abs thumb" style="left:411px;top:934px;width:48px;height:46px" role="img" aria-label="Rider on horseback"></div>
<div class="abs thumb warm" style="left:463px;top:934px;width:48px;height:46px" role="img" aria-label="Sepia group photo"></div>

<!-- quotes -->
<div class="abs divider" style="left:326px;top:1002px;width:78px"></div>
<div class="abs quotes-title">QUOTES</div>
<blockquote class="abs quote" style="left:162px"><div class="avatar" role="img" aria-label="Member portrait"></div><p>Nulla volutpat felis massa, eu viverra libero venenatis in. Sed nec tristique erat, ut fringilla velit. Nunc interdum quis magna at dictum. Nulla volutpat felis massa.<b>Ida Marsh</b></p></blockquote>
<div class="abs" style="left:358px;top:1032px;height:34px;border-left:1px solid var(--rule)"></div>
<blockquote class="abs quote" style="left:387px"><div class="avatar" role="img" aria-label="Member portrait"></div><p>Nulla volutpat felis massa, eu viverra libero venenatis in. Sed nec tristique erat, ut fringilla velit. Nunc interdum quis magna at dictum. Nulla volutpat felis massa.<b>Ida Marsh</b></p></blockquote>
<div class="abs divider" style="left:326px;top:1080px;width:78px"></div>

<!-- footer -->
<footer class="abs footer"></footer>
<div class="abs fcol" style="left:162px"><h4>Explore Drover</h4><ul><li>Why Drover?</li><li>Packages</li><li>Equipment &amp; Features</li><li>Social Media</li></ul></div>
<div class="abs fcol" style="left:248px"><h4>Drover Network</h4><ul><li>Movies</li><li>TV Shows</li><li>Sports</li><li>Networks</li><li>Guide</li></ul></div>
<div class="abs fcol" style="left:326px"><h4>Customer Service</h4><ul><li>Answer Center</li><li>Drover Rebates</li><li>Refer a Friend</li><li>Agreements &amp; Policies</li></ul></div>
<div class="abs fcol" style="left:405px"><h4>We are Social</h4>
  <div class="social"><i></i><u>2.6m</u> Pagebook</div>
  <div class="social"><i></i>@Drover chirpr</div>
  <div class="social"><i></i><u>10k</u> Plusly</div>
</div>
<div class="abs fbrand"><span class="brand-mark"></span>The Drover's Son</div>
<div class="abs" style="left:162px;top:1183px;width:393px;border-top:1px solid rgba(255,255,255,.2)"></div>
<div class="abs legal" style="left:163px">Our Company &nbsp;|&nbsp; Careers &nbsp;|&nbsp; Site Map</div>
<div class="abs legal" style="left:463px">© 2013 Drover Wiki. All rights reserved.</div>

</body>
</html>
```